Redesign of business card for Silverbrook Mechanical

We are looking for a new design for our business cards for Silverbrook Mechanical. We are a plumbing & HVAC construction company, operating on the West Coast of Canada and USA. Logo attached.
Industry/Entity Type
Construction - Plumbing & HVAC
Contact Information for Business Card
Name, address, phone numbers, email, website address
Look and feel

```html
<!DOCTYPE html>
<html lang="en">
<head>
<meta charset="utf-8">
<title>Silverbrook Mechanical – Business Card</title>
<link href="https://fonts.googleapis.com/css2?family=Roboto+Condensed:wght@700&family=Arimo:wght@400&display=swap" rel="stylesheet">
<style>
  :root{
    --backdrop:#dcdcdc;
    --paper:#f4f4f4;
    --ink:#000000;
    --stripe:#6e6e6e;
    --back-card:#323232;
    --light:#ffffff;
  }
  *{margin:0;padding:0;box-sizing:border-box;}
  html,body{width:1200px;height:1040px;overflow:hidden;background:var(--backdrop);}
  .card{position:absolute;left:285px;width:642px;height:366px;border-radius:16px;overflow:hidden;}
  .card--front{top:130px;background:var(--paper);}
  .card--back{top:568px;background:var(--back-card);}
  .card__shapes{position:absolute;inset:0;width:100%;height:100%;}
  .brand{position:absolute;display:flex;align-items:center;gap:12px;
    font-family:"Roboto Condensed",sans-serif;font-weight:700;text-transform:uppercase;line-height:1.05;}
  .brand__mark{flex:none;}
  .card--front .brand{left:52px;top:96px;color:var(--ink);font-size:30px;}
  .card--front .brand__mark{width:18px;height:18px;background:var(--ink);}
  .card--back .brand{left:0;right:0;top:110px;justify-content:center;color:var(--light);font-size:50px;gap:18px;}
  .card--back .brand__mark{width:28px;height:28px;background:var(--light);}
  .contact{position:absolute;right:36px;top:0;text-align:right;color:var(--light);font-family:Arimo,sans-serif;}
  .contact__name{position:absolute;right:0;top:126px;white-space:nowrap;font-family:"Roboto Condensed",sans-serif;font-weight:700;font-size:24px;}
  .contact__title{position:absolute;right:0;top:152px;white-space:nowrap;font-size:15px;}
  .contact__address{position:absolute;right:0;top:207px;white-space:nowrap;font-size:15px;line-height:20px;}
  .contact__lines{position:absolute;right:0;top:266px;list-style:none;font-size:15px;line-height:20px;}
  .contact__lines li{display:flex;justify-content:flex-end;align-items:center;gap:10px;white-space:nowrap;}
  .contact__lines svg{width:13px;height:13px;flex:none;}
  .card__url{position:absolute;left:0;right:0;top:322px;text-align:center;color:var(--light);font-family:Arimo,sans-serif;font-size:15px;}
</style>
</head>
<body>
  <section class="card card--front" aria-label="Card front">
    <svg class="card__shapes" viewBox="0 0 642 366" aria-hidden="true">
      <polygon points="491,0 642,0 642,366 234,366" fill="var(--ink)"/>
      <polygon points="474,0 484,0 219,366 186,366" fill="var(--stripe)"/>
    </svg>
    <div class="brand"><span class="brand__mark"></span><span>Silverbrook<br>Mechanical</span></div>
    <div class="contact" style="width:0;height:366px;">
      <div class="contact__name">Daniel Reyes</div>
      <div class="contact__title">President</div>
      <div class="contact__address">2170 Harbourview Road<br>Bellingham, WA 98225</div>
      <ul class="contact__lines">
        <li>(360) 555-0148
          <svg viewBox="0 0 24 24"><path fill="#fff" d="M6.6 10.8a15.1 15.1 0 0 0 6.6 6.6l2.2-2.2a1 1 0 0 1 1-.25 11.4 11.4 0 0 0 3.6.57 1 1 0 0 1 1 1V20a1 1 0 0 1-1 1A17 17 0 0 1 3 4a1 1 0 0 1 1-1h3.5a1 1 0 0 1 1 1c0 1.25.2 2.45.57 3.57a1 1 0 0 1-.25 1z"/></svg></li>
        <li>name@silverbrookmechanical.com
          <svg viewBox="0 0 24 24"><rect x="2" y="5" width="20" height="14" fill="#fff"/><path d="M2 5l10 8 10-8" fill="none" stroke="#000" stroke-width="2"/></svg></li>
        <li>www.silverbrookmechanical.com
          <svg viewBox="0 0 24 24"><circle cx="12" cy="12" r="10" fill="#fff"/><path d="M2 12h20M12 2c3 3 3 17 0 20M12 2c-3 3-3 17 0 20" fill="none" stroke="#000" stroke-width="1.5"/></svg></li>
      </ul>
    </div>
  </section>

  <section class="card card--back" aria-label="Card back">
    <div class="brand"><span class="brand__mark"></span><span>Silverbrook Mechanical</span></div>
    <div class="card__url">www.silverbrookmechanical.com</div>
  </section>
</body>
</html>
```